Readable, Vibrant Large Shop Front Poster for Tutoring School.

Uncluttered design for the windows of our Business.
It needs to be readable from a distance.
It will be split across two windows. I've uploaded a picture of the premises. The poster is unfortunately split in two- see the shopfront photo - It will be in the two Square windows where the balloons are now.
I've also uploaded our logo which will be used as signage/ on the roof and would like the posters to tie in with it.

What we want to stand out
Over all :
That we are a Tutoring School Specializing in Secondary/KTR Studies

On the left hand side:
- 1 hour lessons are $20 with no joining fees or contracts (casual week to week bookings)

The right hand side:
-Weekly Lessons no contracts
-Summer School
-Holiday Program
-Workshops
-KTR EXAM PREP

Need B0 size (1000mm x 1414mm)

Requirements
Must have
• It must have large clear writing.
Nice to have
• a border top and bottom of the logo swirls, We don't need the business name on this poster.
Should not have
• Not a fan of Purple or Lime Green.

```html
<!DOCTYPE html>
<html lang="en">
<head>
<meta charset="utf-8">
<title>Tutoring School Window Posters</title>
<link rel="stylesheet" href="https://fonts.googleapis.com/css2?family=Anton&display=swap">
<style>
  :root {
    --page-grey: #b2b2b2;
    --ink: #000000;
    --night: #02101c;
    --white: #ffffff;
    --sun: #f9b035;
    --sun-light: #fdd795;
    --flame: #e8501f;
    --flame-light: #ef7049;
    --teal: #26a39e;
    --teal-light: #94d3d0;
    --berry: #d3044f;
    --berry-light: #e97ba6;
    --scarlet: #ec1c24;
    --scarlet-light: #f07073;
  }
  * { margin: 0; padding: 0; box-sizing: border-box; }
  html, body {
    width: 1200px;
    height: 927px;
    overflow: hidden;
    background: var(--page-grey);
  }
  .sheet {
    position: relative;
    width: 1200px;
    height: 927px;
    font-family: "Anton", "Impact", sans-serif;
  }
  .side-label {
    position: absolute;
    top: 26px;
    width: 300px;
    text-align: center;
    font-size: 46px;
    line-height: 1;
    color: var(--ink);
    letter-spacing: -0.5px;
  }
  .side-label--left { left: 177px; }
  .side-label--right { left: 743px; }
  .poster {
    position: absolute;
    top: 108px;
    width: 554px;
    height: 783px;
    background: var(--night);
    overflow: hidden;
  }
  .poster--left { left: 36px; }
  .poster--right { left: 614px; }
  .poster svg { display: block; width: 100%; height: 100%; }
  .poster text { font-family: "Anton", "Impact", sans-serif; }
</style>
</head>
<body>
<main class="sheet">
  <h2 class="side-label side-label--left">LEFT SIDE</h2>
  <h2 class="side-label side-label--right">RIGHT SIDE</h2>

  <section class="poster poster--left" aria-label="Pricing poster">
    <svg viewBox="0 0 554 783" xmlns="http://www.w3.org/2000/svg">
      <defs>
        <linearGradient id="flame-split" x1="0" y1="0" x2="0.06" y2="1">
          <stop offset="0.56" stop-color="var(--flame)"/>
          <stop offset="0.56" stop-color="var(--flame-light)"/>
        </linearGradient>
        <linearGradient id="teal-split" x1="0" y1="0" x2="0.06" y2="1">
          <stop offset="0.6" stop-color="var(--teal)"/>
          <stop offset="0.6" stop-color="var(--teal-light)"/>
        </linearGradient>
        <linearGradient id="berry-split" x1="0" y1="0" x2="0.04" y2="1">
          <stop offset="0.55" stop-color="var(--berry)"/>
          <stop offset="0.55" stop-color="var(--berry-light)"/>
        </linearGradient>
        <radialGradient id="swirl-warm" cx="0.5" cy="0.5" r="0.6">
          <stop offset="0" stop-color="var(--scarlet)" stop-opacity="0.85"/>
          <stop offset="0.5" stop-color="var(--sun)" stop-opacity="0.6"/>
          <stop offset="1" stop-color="var(--teal)" stop-opacity="0"/>
        </radialGradient>
        <radialGradient id="swirl-cool" cx="0.5" cy="0.5" r="0.6">
          <stop offset="0" stop-color="#2a3c9c" stop-opacity="0.85"/>
          <stop offset="0.5" stop-color="var(--berry)" stop-opacity="0.6"/>
          <stop offset="1" stop-color="var(--teal)" stop-opacity="0"/>
        </radialGradient>
        <clipPath id="price-disc-clip">
          <circle cx="272" cy="168" r="136"/>
        </clipPath>
      </defs>

      <g class="swirl-corner" role="img" aria-label="Colourful logo swirl ornament, top left">
        <rect x="0" y="0" width="124" height="128" fill="url(#swirl-warm)"/>
      </g>
      <g class="swirl-corner" role="img" aria-label="Colourful logo swirl ornament, top right">
        <rect x="442" y="0" width="112" height="128" fill="url(#swirl-warm)"/>
      </g>
      <g class="swirl-corner" role="img" aria-label="Colourful logo swirl ornament, bottom left">
        <rect x="0" y="667" width="132" height="116" fill="url(#swirl-cool)"/>
      </g>
      <g class="swirl-corner" role="img" aria-label="Colourful logo swirl ornament, bottom right">
        <rect x="432" y="667" width="122" height="116" fill="url(#swirl-cool)"/>
      </g>

      <g class="price-disc">
        <circle cx="272" cy="168" r="136" fill="var(--sun-light)"/>
        <circle cx="258" cy="158" r="134" fill="var(--sun)" clip-path="url(#price-disc-clip)"/>
        <text class="price" x="272" y="224" text-anchor="middle" font-size="150"
              textLength="206" lengthAdjust="spacingAndGlyphs"
              fill="var(--white)" stroke="#3a2a10" stroke-width="1.5">$20</text>
      </g>

      <text class="headline" x="37" y="407" font-size="88"
            textLength="483" lengthAdjust="spacingAndGlyphs"
            fill="url(#flame-split)">1 HOUR LESSON</text>
      <text class="subline" x="513" y="468" font-size="54" text-anchor="end"
            textLength="318" lengthAdjust="spacingAndGlyphs"
            fill="url(#teal-split)">NO JOINING FEES</text>
      <text class="subline" x="509" y="529" font-size="54" text-anchor="end"
            textLength="301" lengthAdjust="spacingAndGlyphs"
            fill="url(#teal-split)">OR CONTRACTS</text>
      <text class="note" x="47" y="621" font-size="36"
            textLength="461" lengthAdjust="spacingAndGlyphs"
            fill="url(#berry-split)">(CASUAL WEEK TO WEEK BOOKINGS)</text>
    </svg>
  </section>

  <section class="poster poster--right" aria-label="Programs poster">
    <svg viewBox="0 0 555 783" xmlns="http://www.w3.org/2000/svg">
      <defs>
        <filter id="type-shadow" x="-5%" y="-20%" width="110%" height="140%">
          <feDropShadow dx="3" dy="3" stdDeviation="0" flood-color="#000000"/>
        </filter>
        <polygon id="band-shape" points="0,0 555,-28 555,76 0,104"/>
        <polygon id="band-glint" points="144,96.7 555,24 555,76"/>
      </defs>

      <g class="program-band" transform="translate(0 57)">
        <use href="#band-shape" fill="var(--sun)"/>
        <use href="#band-glint" fill="var(--sun-light)"/>
      </g>
      <g class="program-band" transform="translate(0 203)">
        <use href="#band-shape" fill="var(--flame)"/>
        <use href="#band-glint" fill="var(--flame-light)"/>
      </g>
      <g class="program-band" transform="translate(0 350)">
        <use href="#band-shape" fill="var(--teal)"/>
        <use href="#band-glint" fill="var(--teal-light)"/>
      </g>
      <g class="program-band" transform="translate(0 496)">
        <use href="#band-shape" fill="var(--berry)"/>
        <use href="#band-glint" fill="var(--berry-light)"/>
      </g>
      <g class="program-band" transform="translate(0 642)">
        <use href="#band-shape" fill="var(--scarlet)"/>
        <use href="#band-glint" fill="var(--scarlet-light)"/>
      </g>

      <g class="program-labels" fill="var(--white)" filter="url(#type-shadow)" text-anchor="middle">
        <text x="280" y="110" font-size="46" textLength="524" lengthAdjust="spacingAndGlyphs"
              transform="rotate(-2.9 280 92)">WEEKLY LESSONS NO CONTRACTS</text>
        <text x="276" y="271" font-size="82" textLength="419" lengthAdjust="spacingAndGlyphs"
              transform="rotate(-2.9 276 241)">SUMMER SCHOOL</text>
        <text x="274" y="418" font-size="82" textLength="466" lengthAdjust="spacingAndGlyphs"
              transform="rotate(-2.9 274 388)">HOLIDAY PROGRAM</text>
        <text x="281" y="567" font-size="90" textLength="381" lengthAdjust="spacingAndGlyphs"
              transform="rotate(-2.9 281 534)">WORKSHOPS</text>
        <text x="286" y="713" font-size="90" textLength="423" lengthAdjust="spacingAndGlyphs"
              transform="rotate(-2.9 286 680)">KTR EXAM PREP</text>
      </g>
    </svg>
  </section>
</main>
</body>
</html>
```